Infographic on Rock History (but not Rock-and-Roll, unfortunately)

Looking to create an infographic that tells the story of a giant rock that is featured in the architecture of a friend's mountainside home. I have pics of the rock and a geologist's description. Infographic does not need to tell the entire story with all the details - I am looking for a designer to pick out the most interesting, compelling parts of the rock's history and creatively illustrate it - all while keeping it simple.
The entire mountain range is less than 20 million years old, however, the rock is more than 1.75 billion years old. Not surprisingly, the rocks are quite deformed, folded, tilted, metamorphosed, fractured and weathered. The rocks in the house at Wrenfield Lane and Corbel dip about 80 degrees to the southeast.
However, the tilted rocks are quartzite, which happens to be the most physically and chemically resistant rock on earth, made of nearly pure quartz sand grains (chemically equivalent to inert Durolin glass).
The sand grains themselves were eroded from even older terrains of unknown origin, but likely from rocks near Canada or Siberia, rocks themselves at least 2.3 to 3 billion years old. The sand grains were transported by a river to the margin of our North American continent some 1.75 billion years ago and laid down in sheets of well-sorted sand. That is why the layers look so homogenous, albeit fractured.
Deposition continued and the sandy layers were subsequently buried. Over time the sand turned to sandstone. Around 1.65 billion years ago this margin of North America collided with another continent and buckled the crust extensively forming folds, sheared rock, tilted rock and faults. This is a well-known event in Arizona referred to as the Mazatzal Orogeny (named after the Mazatzal Mountains near Rye, AZ).
The sandstone was metamorphosed into quartzite prior to and during this event, a metamorphic rock. Until the Phoenix Mountains formed ~20 million years ago, the tilted quartzite layers have remained essentially in place, tilted as is, and unweathered for nearly 1.7 billion years, which is hard to imagine, but that’s geology. The quartzite on this part of the Preserve represents the top of a thick sequence of metamorphosed sand, mud and volcanic rocks about 8 to 10 miles thick! Okay, that is hard to imagine.
So to summarize, the rock is 1.75 billion-year-old sandstone, made of even older sand grains of unknown origin, metamorphosed ~1.65 billion years ago, buried for ~1.6 billion years until about ~20 million years ago and presently lay exposed to weathering and erosion, and of course, admiration and fascination.
I plan to end the contest early on Monday, September 9 and 8pm ET. If anyone has a problem with that, please let me know and I will consider keeping it through the 10th.
Highly educated adult business professionals
Architecture

```html
<!DOCTYPE html>
<html lang="en">
<head>
<meta charset="utf-8">
<title>What Is This Rock?</title>
<link rel="stylesheet" href="https://fonts.googleapis.com/css2?family=Montserrat:wght@800&family=Roboto+Condensed:wght@300&family=Open+Sans:wght@700;800&family=Arimo:wght@400&display=swap">
<style>
  :root {
    --ground: #38393b;
    --ground-deep: #2f3032;
    --lime: #8fe01c;
    --yellow: #e8f224;
    --text-yellow: #eef26a;
    --white: #ffffff;
    --sky: #e9ecef;
  }
  html, body { margin: 0; padding: 0; background: var(--ground-deep); }
  body { width: 849px; height: 1200px; overflow: hidden; }
  .poster {
    position: relative; width: 849px; height: 1200px; overflow: hidden;
    background: linear-gradient(160deg, var(--ground) 0%, var(--ground-deep) 100%);
    font-family: "Open Sans", sans-serif;
  }
  .poster > * { position: absolute; }
  .frame { left: 0; top: 0; width: 849px; height: 1200px; }

  .headline { left: 528px; top: 352px; margin: 0; color: var(--white); }
  .headline .question { display: block; font: 800 34px/1 "Montserrat", sans-serif; margin-left: 183px; }
  .headline .lead { display: block; font: 800 29px/1 "Montserrat", sans-serif; letter-spacing: -0.5px; }
  .headline .word { display: block; font: 800 76px/0.95 "Montserrat", sans-serif; color: var(--yellow); letter-spacing: -1px; }

  .era-number { font: 300 46px/1 "Roboto Condensed", sans-serif; color: var(--yellow); letter-spacing: -1px; }
  .era-label { font: 800 13.5px/1 "Open Sans", sans-serif; color: var(--yellow); letter-spacing: 0.3px; }
  .rule { height: 10px; background: var(--yellow); opacity: 0.55; }
  .story { margin: 0; font: 700 11.6px/17.4px "Open Sans", sans-serif; color: var(--text-yellow); white-space: nowrap; }

  .place-tag {
    left: 283px; top: 907px; width: 252px; height: 34px; background: var(--lime);
    color: var(--white); font: 400 21px/34px "Arimo", sans-serif; text-indent: 18px;
  }
  .caption { left: 614px; top: 1072px; margin: 0; color: var(--white); font: 400 18.5px/1.08 "Arimo", sans-serif; white-space: nowrap; }
</style>
</head>
<body>
<main class="poster">
  <svg class="frame" viewBox="0 0 849 1200">
    <defs>
      <linearGradient id="cliff-tone" x1="0" y1="0" x2="1" y2="1">
        <stop offset="0" stop-color="#5a4638"/>
        <stop offset="0.45" stop-color="#7a6151"/>
        <stop offset="0.75" stop-color="#4a3a30"/>
        <stop offset="1" stop-color="#8a9a70"/>
      </linearGradient>
      <linearGradient id="range-tone" x1="0" y1="0" x2="0" y2="1">
        <stop offset="0" stop-color="#7f9cc4"/>
        <stop offset="0.5" stop-color="#3e4f80"/>
        <stop offset="1" stop-color="#24305a"/>
      </linearGradient>
      <linearGradient id="city-tone" x1="0" y1="0" x2="0" y2="1">
        <stop offset="0" stop-color="#8aa4cc"/>
        <stop offset="0.55" stop-color="#3b4a7a"/>
        <stop offset="0.8" stop-color="#b4503a"/>
        <stop offset="1" stop-color="#2a2f4a"/>
      </linearGradient>
      <linearGradient id="ledge-tone" x1="0" y1="0" x2="1" y2="1">
        <stop offset="0" stop-color="#8a6f68"/>
        <stop offset="0.5" stop-color="#b29a92"/>
        <stop offset="1" stop-color="#6e5650"/>
      </linearGradient>
      <linearGradient id="layers-tone" x1="0" y1="0" x2="0" y2="1">
        <stop offset="0" stop-color="#f2f2f2"/>
        <stop offset="0.55" stop-color="#e6807c"/>
        <stop offset="1" stop-color="#8c4a55"/>
      </linearGradient>
      <linearGradient id="plate-tone" x1="0" y1="0" x2="0" y2="1">
        <stop offset="0" stop-color="#eee6dd"/>
        <stop offset="1" stop-color="#cf6a2a"/>
      </linearGradient>
    </defs>

    <polygon role="img" aria-label="Photograph of the tilted, fractured quartzite rock face on the hillside"
      fill="url(#cliff-tone)"
      points="0,0 849,0 849,178 780,215 740,192 665,350 545,282 300,425 180,395 0,495"/>

    <polyline fill="none" stroke="var(--lime)" stroke-width="12" stroke-linejoin="miter"
      points="-6,498 180,395 300,425 545,282 665,350 740,192 780,215 856,174"/>
    <polyline fill="none" stroke="var(--lime)" stroke-width="12" stroke-linejoin="miter"
      points="130,1206 330,1066 560,1040 700,985 760,1000 856,940"/>

    <rect role="img" aria-label="Illustration of a weathering rock shedding sand grains" x="40" y="500" width="90" height="64" fill="#cdcdcd"/>
    <rect role="img" aria-label="Illustration of a river carrying sand to a map of North America" x="412" y="490" width="128" height="110" rx="8" fill="#d8e4e4"/>
    <rect role="img" aria-label="Illustration of stacked sandy layers" x="102" y="628" width="112" height="56" rx="8" fill="url(#layers-tone)"/>
    <rect role="img" aria-label="Diagram of two continental plates colliding" x="484" y="684" width="160" height="70" fill="url(#plate-tone)"/>
    <rect role="img" aria-label="Speckled granite texture mound" x="30" y="880" width="214" height="52" rx="10" fill="#c8c8c8"/>

    <circle role="img" aria-label="Photograph of the Phoenix Mountains" cx="765" cy="850" r="122" fill="url(#range-tone)" stroke="var(--lime)" stroke-width="9"/>
    <circle role="img" aria-label="Photograph of the Phoenix Mountains above the city at dusk" cx="630" cy="912" r="84" fill="url(#city-tone)" stroke="var(--lime)" stroke-width="9"/>
    <circle role="img" aria-label="Close photograph of the layered quartzite surface" cx="440" cy="1085" r="80" fill="url(#ledge-tone)" stroke="var(--lime)" stroke-width="9"/>

    <polyline fill="none" stroke="var(--yellow)" stroke-width="3" stroke-linejoin="miter"
      points="532,1068 548,1076 556,1068 575,1084 590,1078 604,1084"/>
  </svg>

  <h1 class="headline">
    <span class="question">?</span>
    <span class="lead">WHAT IS THIS</span>
    <span class="word">ROCK</span>
  </h1>

  <div class="era-number" style="left:100px; top:468px;">1.75</div>
  <div class="era-label" style="left:173px; top:468px;">BILLION YEARS AGO</div>
  <div class="rule" style="left:173px; top:489px; width:240px;"></div>
  <p class="story" style="left:173px; top:507px;">Corroded sand particles from Rocks<br>near Canada or Siberia were<br>transported to the margins of North<br>American Continent by rivers</p>

  <div class="rule" style="left:250px; top:609px; width:216px;"></div>
  <p class="story" style="left:250px; top:629px;">They started getting deposited over<br>each other in form of sandy layers<br>and were subsequently buried.<br>Overtime the sand turned into sand<br>stone.</p>

  <div class="era-number" style="left:228px; top:740px;">1.65</div>
  <div class="era-label" style="left:305px; top:743px;">BILLION YEARS AGO</div>
  <div class="rule" style="left:305px; top:766px; width:240px;"></div>
  <p class="story" style="left:308px; top:790px;">This margin of the american continent<br>collided with another continent plate<br>which folded the american plate<br>leading to shearing of rocks, tilting of<br>rocks and fault formation. This is also<br>known as Mazatzal Orogeny.</p>

  <div class="place-tag">Phoenix Mountains</div>

  <div class="era-number" style="left:30px; top:940px; letter-spacing:1px;">200</div>
  <div class="era-label" style="left:110px; top:942px;">MILLION YEARS AGO</div>
  <div class="rule" style="left:110px; top:965px; width:240px;"></div>
  <p class="story" style="left:110px; top:988px;">The sand stone got metamorphized<br>into quartze. Until the phoenix<br>mountains formed around 20 million<br>years ago, the tilted rocks remained in<br>place unweathered.</p>

  <p class="caption">This rock represents<br>the top layer of the<br>rocks which are 8 to<br>10 miles thick.</p>
</main>
</body>
</html>
```